Webdesign for a business that converts shops into apps. UPDATE BRIEF

We want a creative/professional design for our new business Quindo.

Quindo is a service that can deliver instant apps for brellix shops. So every shop owner can have its own app for selling to there customers.

We are open for your interpretation of the design. We think it could be intersting doing an onepage design for this. But thats not set in stones offcourse.

We need several section:
top section
some facts abt the service and maybe our company
price table
some customer review
functionalitys of the app (in a nice way shown)
Section showing screens of a demo shop.
footer with ccdetails, socialmedia, newsletter

I have been playing abit myself with a theme, but no development/designer experience. And we really need a very professional and custom look.

Ps. we are an ecommerce company so if we find any good designer here, we will have enough work for you.

Some competitors in this field;

http://lnk.example-short.net/7hTq2Wz
http://lnk.example-short.net/4kRv9Jd

Here is a design we like
http://tovelapp.example.com/

Hoping for some great concepts!

Kind Regards and good luck!

Some screenshots which can be used for app demo;

UPDATE BRIEF

We would like to add a section for features of the app.
We would like to show a zelphone screen and all the most important features of the app and when clicking every feature the screen would change or the feature intened would be high lighted in some way.

The features and any content and info abt that can be used from
https://www.norvapp-example.com/features.html/

We need an how it works section aswell in the design, also that can be used content from here
https://www.norvapp-example.com/how-it-works/

Norvapp is our partner, so there work way and features are same as ours. We just want it in a different 'look and feel/design)

Reason: Getting very few good design at the moment. Same designers seem to be responding whith 5 designs at a time of low quality.

Target Market(s)

brellix webshop

Industry/Entity Type

Business

Number of Pages Required

1 page

Font styles to use
Sans Serif

Colors
0355a3
3176b5
85acd3
85cae6
33a6d7
0392cd
f59195
33b8a4

Requirements
Must have
• a creative and custom look, not a copied theme vibe.
Nice to have
• it would be nice if the entire design has a nice flow goinf through the site. The customers experience should be on point.
Should not have
• boring static experience

```html
<!DOCTYPE html>
<html lang="en">
<head>
<meta charset="utf-8">
<title>Quindo – instant apps for Brellix shops</title>
<link rel="stylesheet" href="https://fonts.googleapis.com/css2?family=Michroma&family=Open+Sans:wght@400;600;700&family=Roboto:wght@400;500;700;900&display=swap">
<style>
:root{
  --navy:#0355a3;
  --blue:#3176b5;
  --blue-soft:#85acd3;
  --sky:#85cae6;
  --cyan:#52cbe6;
  --cyan-deep:#33a6d7;
  --azure:#0392cd;
  --pink:#f59195;
  --green:#33b8a4;
  --plan-basic:#6fbde6;
  --grey-bg:#ececec;
  --card-grey:#e6e6e6;
  --ink:#1c1c1c;
  --text:#555;
  --white:#fff;
}
*{margin:0;padding:0;box-sizing:border-box}
html,body{width:1200px;height:4467px;overflow:hidden}
body{position:relative;background:var(--white);font-family:"Open Sans",Arial,sans-serif;color:var(--text)}
.abs{position:absolute}
.display{font-family:"Michroma","Arial Black",sans-serif;text-transform:uppercase}
.doc-icon{position:absolute;width:36px;height:36px;background:var(--azure);display:flex;align-items:center;justify-content:center}
.placeholder{position:absolute}

/* header */
.site-header{position:absolute;left:0;top:0;width:1200px;height:150px;background:var(--white)}
.brand{position:absolute;left:134px;top:20px;font-family:"Roboto",sans-serif;font-weight:500;font-size:74px;line-height:1;color:var(--navy);letter-spacing:-1px}
.newsletter-btn{position:absolute;left:858px;top:21px;width:205px;height:45px;background:var(--azure);color:var(--white);font:700 14px "Roboto",sans-serif;display:flex;align-items:center}
.newsletter-btn .mark{width:45px;height:45px;background:var(--white);border:3px solid var(--azure);display:flex;align-items:center;justify-content:center;margin-right:22px}
.main-nav{position:absolute;left:596px;top:88px;display:flex;gap:34px;font:500 14px "Roboto",sans-serif;color:var(--ink)}
.header-bar{position:absolute;left:134px;top:120px;width:932px;height:12px;background:var(--navy)}

/* hero */
.hero{position:absolute;left:0;top:155px;width:1200px;height:792px;background:linear-gradient(135deg,#3f88c6,#3176b5 55%,#2d6cab);overflow:hidden}
.hero-account{position:absolute;right:134px;top:20px;font:500 13px "Roboto",sans-serif;color:var(--white);display:flex;gap:30px}
.slider-arrows{position:absolute;display:flex;gap:8px}
.slider-arrows span{width:26px;height:26px;border-radius:50%;background:var(--sky);display:flex;align-items:center;justify-content:center}
.hero-title{position:absolute;left:587px;top:232px;font-size:56px;line-height:1;color:var(--white);letter-spacing:1px;white-space:nowrap}
.hero-lead{position:absolute;left:587px;top:383px;width:500px;font:700 27px/1.3 "Roboto",sans-serif;color:var(--white)}
.hero-sub{position:absolute;left:587px;top:470px;font-size:16px;color:var(--white)}
.dots{position:absolute;display:flex;gap:10px}
.dots i{width:18px;height:18px;border-radius:50%;background:var(--blue-soft)}
.dots i.on{background:var(--white)}
.cta{position:absolute;left:709px;top:598px;width:232px;height:66px;border:3px solid var(--white);border-radius:33px;color:var(--white);font:500 28px "Roboto",sans-serif;display:flex;align-items:center;justify-content:center}

/* about */
.about{position:absolute;left:0;top:959px;width:1200px;height:420px;background:var(--grey-bg);overflow:hidden}
.about h2{position:absolute;left:137px;top:40px;font:900 28px/1.2 "Roboto",sans-serif;color:var(--ink);text-transform:uppercase}
.about h3{position:absolute;left:137px;top:138px;font:600 17px/1.35 "Open Sans",sans-serif;color:var(--azure)}
.about p{position:absolute;z-index:2;left:137px;top:208px;width:720px;font-size:14px;line-height:1.55;color:#444}
.about-phone{position:absolute;left:0;top:0;width:1200px;height:420px;z-index:1;background:linear-gradient(135deg,#ffffff,#d3d8dc);clip-path:polygon(1060px 180px,1200px 205px,1200px 420px,640px 420px,590px 392px)}

/* pricing */
.pricing{position:absolute;left:0;top:1412px;width:1200px;height:464px;background:var(--cyan)}
.plan{position:absolute;top:68px;width:283px;height:331px;background:var(--white)}
.plan-head{height:69px;padding:14px 24px;font:900 19px/1.2 "Roboto",sans-serif;text-transform:uppercase}
.plan-head small{display:block;font-size:19px;color:var(--white)}
.plan ul{list-style:none;padding:40px 24px 0}
.plan li{display:flex;justify-content:space-between;font-size:15px;height:42px;color:var(--azure)}
.plan li b{color:#333;font-weight:700}
.plan-foot{position:absolute;left:0;bottom:0;width:100%;height:33px}
.plan-foot .doc-icon{left:0;top:-3px}
.plan.basic .plan-head{background:var(--plan-basic);color:var(--navy)}
.plan.basic .plan-foot{background:var(--plan-basic)}
.plan.plus .plan-head{background:var(--green);color:#0d3d36}
.plan.plus .plan-foot{background:var(--green)}
.plan.extra .plan-head{background:var(--pink);color:#8a1f24}
.plan.extra .plan-foot{background:var(--pink)}

/* reviews */
.reviews{position:absolute;left:0;top:1876px;width:1200px;height:536px;background:var(--white)}
.review{position:absolute;top:63px;width:295px;height:464px;background:var(--card-grey)}
.review .photo{position:absolute;left:0;top:0;width:100%;height:175px}
.review h4{position:absolute;left:46px;top:207px;font:700 15px "Roboto",sans-serif;color:var(--azure);text-transform:uppercase}
.review .quote{position:absolute;right:38px;top:192px;font:900 60px/1 "Roboto",sans-serif;color:var(--azure)}
.review p{position:absolute;left:24px;top:285px;width:247px;font-size:14px;line-height:1.5;text-align:center;color:#444}
.review .doc-icon{left:0;bottom:0}

/* tool */
.tool{position:absolute;left:0;top:2448px;width:1200px;height:470px;background:var(--cyan);overflow:hidden}
.tool-num{position:absolute;left:538px;top:210px;font:500 72px/1 "Roboto",sans-serif;color:var(--white)}
.tool h3{position:absolute;left:655px;top:226px;font:500 28px/1.1 "Roboto",sans-serif;color:var(--white);text-transform:uppercase}
.tool p{position:absolute;left:655px;top:320px;width:410px;font-size:14px;line-height:1.5;color:#d7f3fb}

/* demo */
.demo{position:absolute;left:0;top:2948px;width:1200px;height:730px;background:var(--white)}
.shot{position:absolute;width:187px;height:334px;background:linear-gradient(#f7f7f7,#e2e2e2);border:1px solid #ddd}
.shot::before{content:"";position:absolute;left:0;top:0;width:100%;height:14px;background:#333}
.demo h2{position:absolute;left:357px;top:470px;font-size:30px;color:var(--azure);white-space:nowrap}
.demo p{position:absolute;left:357px;top:530px;width:712px;font-size:13.5px;line-height:1.5;color:#333;text-transform:uppercase}
.demo .doc-icon{left:357px;top:682px}

/* features */
.features{position:absolute;left:0;top:3713px;width:1200px;height:552px;background:linear-gradient(#5ccfe8,var(--cyan))}
.features h2{position:absolute;left:137px;top:54px;font-size:30px;color:var(--white)}
.feature{position:absolute;top:155px;width:290px}
.feature h4{position:absolute;top:125px;font:700 17px "Roboto",sans-serif;color:var(--white);text-transform:uppercase}
.feature p{position:absolute;top:168px;width:290px;font-size:13px;line-height:1.55;color:var(--white);text-transform:uppercase;text-align:justify}
.feature .doc-icon{top:320px;left:0}
.to-top{position:absolute;left:1030px;top:4262px;width:34px;height:34px;border-radius:50%;background:var(--azure);display:flex;align-items:center;justify-content:center}

/* footer */
.site-footer{position:absolute;left:0;top:4265px;width:1200px;height:202px;background:var(--white)}
.site-footer .brand{top:40px;left:134px}
.legal{position:absolute;left:137px;top:157px;font-size:12px;color:#333}
.footer-title{position:absolute;top:96px;font:700 14px "Roboto",sans-serif;color:var(--ink);text-transform:uppercase}
.email-field{position:absolute;left:417px;top:134px;width:238px;height:32px;border:1px solid #cfcfcf;font-size:12px;color:#aaa;padding:8px 12px}
.subscribe{position:absolute;left:664px;top:134px;width:96px;height:32px;background:var(--green);color:var(--white);font:700 12px "Roboto",sans-serif;display:flex;align-items:center;justify-content:center}
.social{position:absolute;left:855px;top:130px;display:flex;gap:12px}
.social i{width:36px;height:36px;border-radius:50%;background:var(--azure)}
</style>
</head>
<body>

<header class="site-header">
  <div class="brand">quindo</div>
  <div class="newsletter-btn">
    <span class="mark"><svg width="22" height="16" viewBox="0 0 22 16"><rect x="1" y="1" width="20" height="14" fill="none" stroke="#0392cd" stroke-width="2"/><path d="M1 1l10 8 10-8" fill="none" stroke="#0392cd" stroke-width="2"/></svg></span>
    NEWSLETTER
  </div>
  <nav class="main-nav"><span>HOME</span><span>ABOUT</span><span>SERVICE</span><span>BLOG</span><span>FETURED</span></nav>
  <div class="header-bar"></div>
</header>

<section class="hero">
  <div class="hero-account"><span>&#9906;&nbsp; LOG IN</span><span>|</span><span>SIGN UP &raquo;</span></div>
  <div class="slider-arrows" style="left:1006px;top:60px">
    <span><svg width="10" height="10" viewBox="0 0 10 10"><path d="M7 1L3 5l4 4" fill="none" stroke="#0355a3" stroke-width="2"/></svg></span>
    <span><svg width="10" height="10" viewBox="0 0 10 10"><path d="M3 1l4 4-4 4" fill="none" stroke="#0355a3" stroke-width="2"/></svg></span>
  </div>
  <div class="placeholder" role="img" aria-label="Hand holding a zelphone showing the Quindo app start screen" style="left:232px;top:98px;width:280px;height:694px;border-radius:40px 40px 0 0;background:linear-gradient(#e9ecef,#c9d0d6)">
    <div style="position:absolute;left:30px;top:90px;width:220px;height:400px;background:linear-gradient(#2a74c9,#1d5fae)"></div>
  </div>
  <h1 class="hero-title display">Welcome!</h1>
  <p class="hero-lead">Grow your business brilliantly with Brellixmobile app!</p>
  <p class="hero-sub">Get high conversion. Grow customer loyalty. Earn big revenue.</p>
  <div class="dots" style="left:591px;top:526px"><i class="on"></i><i></i><i></i></div>
  <a class="cta">Sign Me Up</a>
</section>

<section class="about">
  <div class="about-phone" role="img" aria-label="Tilted phone showing a demo shop app home screen"></div>
  <h2>Shortly<br>about us</h2>
  <h3>Create a professional image<br>for Brellix Oriel OS &amp; Droidex Apps</h3>
  <p>Customize your mobile store design in just a few clicks. Make your app completely stand out with two beautiful themes inspired by modern &amp; flat design. Each button optimized. Seeing is believing - give customers that extra vote of confidence in your business.</p>
  <div class="doc-icon" style="left:137px;top:304px;z-index:2"><svg width="16" height="18" viewBox="0 0 16 18"><path d="M2 1h8l4 4v12H2z" fill="none" stroke="#fff" stroke-width="1.6"/><path d="M5 9h6M5 12h6" stroke="#fff" stroke-width="1.4"/></svg></div>
</section>

<section class="pricing">
  <div class="plan basic" style="left:137px">
    <div class="plan-head">Basic<small>Free</small></div>
    <ul><li>E-mails per day<b>40</b></li><li>Web pages per day<b>20</b></li><li>Photos/files per day<b>4</b></li><li>Minutes streaming video<b>10</b></li></ul>
    <div class="plan-foot"><span class="doc-icon"><svg width="16" height="18" viewBox="0 0 16 18"><path d="M2 1h8l4 4v12H2z" fill="none" stroke="#fff" stroke-width="1.6"/><path d="M5 9h6M5 12h6" stroke="#fff" stroke-width="1.4"/></svg></span></div>
  </div>
  <div class="plan plus" style="left:465px">
    <div class="plan-head">Plus<small>2.00 mo</small></div>
    <ul><li>E-mails per day<b>60</b></li><li>Web pages per day<b>50</b></li><li>Photos/files per day<b>9</b></li><li>Minutes streaming video<b>20</b></li></ul>
    <div class="plan-foot"><span class="doc-icon"><svg width="16" height="18" viewBox="0 0 16 18"><path d="M2 1h8l4 4v12H2z" fill="none" stroke="#fff" stroke-width="1.6"/><path d="M5 9h6M5 12h6" stroke="#fff" stroke-width="1.4"/></svg></span></div>
  </div>
  <div class="plan extra" style="left:780px">
    <div class="plan-head">Extra<small>$5.50</small></div>
    <ul><li>E-mails per day<b>90</b></li><li>Web pages per day<b>80</b></li><li>Photos/files per day<b>12</b></li><li>Minutes streaming video<b>30</b></li></ul>
    <div class="plan-foot"><span class="doc-icon"><svg width="16" height="18" viewBox="0 0 16 18"><path d="M2 1h8l4 4v12H2z" fill="none" stroke="#fff" stroke-width="1.6"/><path d="M5 9h6M5 12h6" stroke="#fff" stroke-width="1.4"/></svg></span></div>
  </div>
</section>

<section class="reviews">
  <article class="review" style="left:137px">
    <div class="photo" role="img" aria-label="Portrait photo of a smiling customer in a hat" style="background:linear-gradient(#8a8a8a,#4a4a4a)"></div>
    <h4>Dorian Falke</h4><span class="quote">&#8220;</span>
    <p>I am really happy because i am using this app, all of their customer service guys are friendly and helpful</p>
    <span class="doc-icon"><svg width="16" height="18" viewBox="0 0 16 18"><path d="M2 1h8l4 4v12H2z" fill="none" stroke="#fff" stroke-width="1.6"/><path d="M5 9h6M5 12h6" stroke="#fff" stroke-width="1.4"/></svg></span>
  </article>
  <article class="review" style="left:453px">
    <div class="photo" role="img" aria-label="Photo of a businessman working at his desk" style="background:linear-gradient(#f1f1f1,#bdbdbd)"></div>
    <h4>Milo Haverton</h4><span class="quote">&#8220;</span>
    <p>hey guys are just awesome, very friendly support, always left you smiling, Special thanks to marlow Keep it up :)</p>
    <span class="doc-icon"><svg width="16" height="18" viewBox="0 0 16 18"><path d="M2 1h8l4 4v12H2z" fill="none" stroke="#fff" stroke-width="1.6"/><path d="M5 9h6M5 12h6" stroke="#fff" stroke-width="1.4"/></svg></span>
  </article>
  <article class="review" style="left:768px">
    <div class="photo" role="img" aria-label="Portrait photo of a smiling customer" style="background:linear-gradient(#f4e4da,#c99a82)"></div>
    <h4>Renata Oslow</h4><span class="quote">&#8220;</span>
    <p>nice solution to synchronise store with mobile application, we are happy to use this solution</p>
    <span class="doc-icon"><svg width="16" height="18" viewBox="0 0 16 18"><path d="M2 1h8l4 4v12H2z" fill="none" stroke="#fff" stroke-width="1.6"/><path d="M5 9h6M5 12h6" stroke="#fff" stroke-width="1.4"/></svg></span>
  </article>
</section>

<section class="tool">
  <div class="placeholder" role="img" aria-label="Tilted phone showing a demo shop product grid" style="left:90px;top:60px;width:380px;height:520px;border-radius:44px;transform:rotate(-22deg);background:linear-gradient(#f3f5f6,#cfd6da)"></div>
  <svg class="abs" style="left:679px;top:33px" width="131" height="140" viewBox="0 0 131 140">
    <g fill="#0355a3">
      <circle cx="65" cy="14" r="12"/><path d="M45 52a20 20 0 0 1 40 0z"/>
      <rect x="63" y="56" width="4" height="22"/><rect x="17" y="76" width="97" height="4"/>
      <rect x="17" y="76" width="4" height="14"/><rect x="63" y="76" width="4" height="14"/><rect x="110" y="76" width="4" height="14"/>
      <circle cx="19" cy="102" r="10"/><path d="M2 136a17 17 0 0 1 34 0z"/>
      <circle cx="65" cy="102" r="10"/><path d="M48 136a17 17 0 0 1 34 0z"/>
      <circle cx="112" cy="102" r="10"/><path d="M95 136a17 17 0 0 1 34 0z"/>
    </g>
  </svg>
  <div class="tool-num">01</div>
  <h3>Powerful tool<br>for your business</h3>
  <p>Multifunctional Brellix apps help you to implement marketing, sales and customer success activities on mobile effectively with ease.</p>
  <div class="dots" style="left:673px;top:426px"><i class="on"></i><i style="background:#a79ad6"></i><i style="background:#a79ad6"></i><i style="background:#a79ad6"></i><i style="background:#a79ad6"></i><i style="background:#a79ad6"></i><i style="background:#a79ad6"></i></div>
  <div class="slider-arrows" style="left:998px;top:422px">
    <span style="background:#7b6cc4"><svg width="10" height="10" viewBox="0 0 10 10"><path d="M7 1L3 5l4 4" fill="none" stroke="#fff" stroke-width="2"/></svg></span>
    <span style="background:#7b6cc4"><svg width="10" height="10" viewBox="0 0 10 10"><path d="M3 1l4 4-4 4" fill="none" stroke="#fff" stroke-width="2"/></svg></span>
  </div>
</section>

<section class="demo">
  <div class="shot" role="img" aria-label="Demo shop screen with category photo grid" style="left:137px;top:18px"></div>
  <div class="shot" role="img" aria-label="Demo shop screen with product list" style="left:381px;top:18px"></div>
  <div class="shot" role="img" aria-label="Demo shop checkout screen" style="left:628px;top:18px"></div>
  <div class="shot" role="img" aria-label="Demo shop product detail screen" style="left:876px;top:18px"></div>
  <div class="shot" role="img" aria-label="Demo shop cart screen" style="left:137px;top:381px"></div>
  <h2 class="display">Showing screens of a demo</h2>
  <p>Vestibulum iaculis lacinia est. Proin dictum elementum velit. Fusce euismod consequat ante. Lorem ipsum sit amet con seetuer adipiscing elit. Pellentesqolor lobortis quis lobortis dignissimquinar ac lorem. Vestibue sed dolor.</p>
  <span class="doc-icon"><svg width="16" height="18" viewBox="0 0 16 18"><path d="M2 1h8l4 4v12H2z" fill="none" stroke="#fff" stroke-width="1.6"/><path d="M5 9h6M5 12h6" stroke="#fff" stroke-width="1.4"/></svg></span>
  <div class="slider-arrows" style="left:953px;top:642px">
    <span style="background:var(--azure)"><svg width="10" height="10" viewBox="0 0 10 10"><path d="M7 1L3 5l4 4" fill="none" stroke="#fff" stroke-width="2"/></svg></span>
    <span style="background:var(--azure)"><svg width="10" height="10" viewBox="0 0 10 10"><path d="M3 1l4 4-4 4" fill="none" stroke="#fff" stroke-width="2"/></svg></span>
  </div>
  <div class="dots" style="left:958px;top:688px"><i style="background:#7ea6d3"></i><i style="background:#7ea6d3"></i><i style="background:#7ea6d3"></i><i style="background:#7ea6d3"></i></div>
</section>

<section class="features">
  <h2 class="display">Features of the app</h2>
  <div class="feature" style="left:137px">
    <svg width="96" height="80" viewBox="0 0 96 80"><g fill="none" stroke="#fff" stroke-width="4"><rect x="22" y="4" width="70" height="46"/><rect x="12" y="16" width="70" height="46"/></g><rect x="2" y="28" width="70" height="46" fill="#fff"/></svg>
    <h4>Native app</h4>
    <p>At Norvapp you have a comprehensive solution to create a native app downloadable on app stores. Native app perform best at loading speed, smooth interaction and function with ease</p>
    <span class="doc-icon"><svg width="16" height="18" viewBox="0 0 16 18"><path d="M2 1h8l4 4v12H2z" fill="none" stroke="#fff" stroke-width="1.6"/><path d="M5 9h6M5 12h6" stroke="#fff" stroke-width="1.4"/></svg></span>
  </div>
  <div class="feature" style="left:456px">
    <svg width="82" height="82" viewBox="0 0 82 82"><circle cx="41" cy="41" r="39" fill="#fff"/><g fill="none" stroke="#52cbe6" stroke-width="3"><ellipse cx="41" cy="41" rx="16" ry="39"/><path d="M2 41h78M8 22h66M8 60h66"/></g></svg>
    <h4>Localization</h4>
    <p>Your app could be displayed at any language or currency. Customers can choose their familiar language or currency when shopping on app</p>
    <span class="doc-icon"><svg width="16" height="18" viewBox="0 0 16 18"><path d="M2 1h8l4 4v12H2z" fill="none" stroke="#fff" stroke-width="1.6"/><path d="M5 9h6M5 12h6" stroke="#fff" stroke-width="1.4"/></svg></span>
  </div>
  <div class="feature" style="left:777px">
    <svg width="56" height="88" viewBox="0 0 56 88"><rect x="3" y="3" width="50" height="82" rx="8" fill="none" stroke="#fff" stroke-width="4"/><path d="M3 16h50M3 70h50" stroke="#fff" stroke-width="3"/><circle cx="28" cy="78" r="3" fill="#fff"/><path d="M12 44h8l4-10 6 18 4-8h10" fill="none" stroke="#fff" stroke-width="3"/></svg>
    <h4>App design</h4>
    <p>You can dress up your app with 3 options of beautiful theme. The smart and modern layout streamlines information and help customers navigate on app easily</p>
    <span class="doc-icon"><svg width="16" height="18" viewBox="0 0 16 18"><path d="M2 1h8l4 4v12H2z" fill="none" stroke="#fff" stroke-width="1.6"/><path d="M5 9h6M5 12h6" stroke="#fff" stroke-width="1.4"/></svg></span>
  </div>
</section>

<footer class="site-footer">
  <div class="brand">quindo</div>
  <p class="legal">QUINDO © 2016 • PRIVACY POLICY</p>
  <h5 class="footer-title" style="left:417px">Newsletter</h5>
  <div class="email-field">Email address</div>
  <div class="subscribe">SUBCRIBE</div>
  <h5 class="footer-title" style="left:855px">Social links</h5>
  <div class="social"><i></i><i></i><i></i><i></i><i></i></div>
</footer>

<div class="to-top"><svg width="14" height="10" viewBox="0 0 14 10"><path d="M1 8l6-6 6 6" fill="none" stroke="#fff" stroke-width="2"/></svg></div>

</body>
</html>
```